Norvik9 custom graphic website icons

We would like unique graphic design icons/illustrations that support our website content for the products and services we offer. We would like a suite of 20-30 unique icons/illustrations to be used on our website and for powerpoint presentations etc... and aligned with our brand logo. Each icon/illustration relates to the relevant content on our website. We would like these icons to have a 'corporate feel' and create a sense of uniqueness in terms of look and feel. You can see current placeholder icons at www.norvik9.example.
Target Market(s)
Large travel and lifestyle vendors i.e. airlines, airports, hotels & travellers/consumers.
Industry/Entity Type
Travel and lifestyle.
Font styles to use
Other font styles liked:
- Avenir
Requirements
Must have
- Icons need to be unique and have a fun but professional/corporate feel.
Nice to have
- A unique character icon to complement non character icons.

```html
<!DOCTYPE html>
<html lang="en">
<head>
<meta charset="utf-8">
<title>Norvik9 – Something about us</title>
<link href="https://fonts.googleapis.com/css2?family=Open+Sans:wght@700&family=Varela+Round&family=Nunito:wght@400&display=swap" rel="stylesheet">
<style>
  :root {
    --page: #ffffff;
    --panel: #e1ecec;
    --ink: #1c3344;
    --heading: #174c55;
    --body: #3c4f58;
    --accent: #2b9a94;
    --track: #f1f1f1;
    --thumb: #c4c4c4;
    --venn-top: #5aa8a6;
    --venn-left: #7b9aa2;
    --venn-right: #0b5557;
    --venn-bottom: #1f8a86;
  }
  * { box-sizing: border-box; margin: 0; padding: 0; }
  html, body { width: 1033px; height: 1200px; overflow: hidden; background: var(--page); }
  body { position: relative; font-family: "Varela Round", sans-serif; color: var(--body); }

  .icon-row { position: absolute; top: 95px; left: 0; width: 1033px; height: 82px; }
  .icon-row svg { position: absolute; top: 0; width: 82px; height: 82px; }

  .icon { fill: none; stroke: var(--ink); stroke-width: 2.4; stroke-linecap: round; stroke-linejoin: round; }

  .panel { position: absolute; left: 34px; width: 965px; height: 441px; background: var(--panel); }
  .panel-values { top: 266px; }
  .panel-services { top: 721px; }

  .scrollbar { position: absolute; right: 0; top: 0; width: 11px; height: 100%; background: var(--track); }
  .scrollbar::before, .scrollbar::after { content: ""; position: absolute; left: 3px; border-left: 2.5px solid transparent; border-right: 2.5px solid transparent; }
  .scrollbar::before { top: 5px; border-bottom: 3px solid #555; }
  .scrollbar::after { bottom: 5px; border-top: 3px solid #555; }
  .scrollbar .thumb { position: absolute; left: 1px; width: 9px; background: var(--thumb); }

  .to-top { position: absolute; left: 902px; width: 30px; height: 30px; background: var(--accent); }
  .to-top svg { width: 30px; height: 30px; }

  .section-title { position: absolute; top: 278px; left: 0; width: 100%; text-align: center; font-family: "Open Sans", sans-serif; font-weight: 700; font-size: 23px; color: var(--heading); letter-spacing: 0.3px; }
  .section-lead { position: absolute; top: 319px; left: 0; width: 100%; text-align: center; font-size: 14px; color: var(--heading); }

  .value { position: absolute; top: 398px; width: 230px; }
  .value svg { display: block; margin: 0 auto; width: 88px; height: 88px; }
  .value h3 { margin-top: 38px; text-align: center; font-family: "Open Sans", sans-serif; font-weight: 700; font-size: 17px; color: var(--heading); }
  .value ul { margin-top: 30px; padding-left: 26px; font-size: 11.4px; line-height: 17px; color: var(--body); }

  .venn { position: absolute; left: 128px; top: 772px; width: 370px; height: 372px; }
  .venn-label { position: absolute; color: #fff; font-family: "Nunito", sans-serif; text-align: center; line-height: 1.05; }

  .feature { position: absolute; left: 520px; width: 400px; }
  .feature svg { position: absolute; left: 0; top: 0; width: 38px; height: 38px; }
  .feature h4 { margin-left: 46px; font-family: "Open Sans", sans-serif; font-weight: 700; font-size: 17px; color: var(--heading); }
  .feature p { margin: 8px 0 0 46px; font-size: 11.4px; line-height: 17px; color: var(--body); width: 345px; }
</style>
</head>
<body>

<div class="icon-row">
  <svg viewBox="0 0 80 80" style="left:118px"><use href="#i-handshake"/></svg>
  <svg viewBox="0 0 80 80" style="left:260px"><use href="#i-team"/></svg>
  <svg viewBox="0 0 80 80" style="left:403px"><use href="#i-person"/></svg>
  <svg viewBox="0 0 80 80" style="left:546px"><use href="#i-shield"/></svg>
  <svg viewBox="0 0 80 80" style="left:688px"><use href="#i-scale"/></svg>
  <svg viewBox="0 0 80 80" style="left:832px"><use href="#i-globe"/></svg>
</div>

<svg width="0" height="0" style="position:absolute">
  <defs>
    <g id="i-handshake" class="icon">
      <path d="M34 22 C24 6 4 10 4 28 C4 40 14 50 22 58"/>
      <path d="M46 22 C56 6 76 10 76 28 C76 40 66 52 56 62"/>
      <path d="M46 22 L34 32 C31 35 34 40 38 37 L48 30 L64 50 C67 54 63 58 59 55 L50 47"/>
      <path d="M59 55 C61 59 57 63 53 60 L46 53"/>
      <path d="M53 60 C55 64 51 67 47 64 L42 59"/>
      <circle cx="22" cy="50" r="3.5"/><circle cx="27" cy="55" r="3.5"/>
      <circle cx="32" cy="60" r="3.5"/><circle cx="38" cy="65" r="3.5"/>
    </g>
    <g id="i-team" class="icon">
      <circle cx="40" cy="26" r="9"/><circle cx="17" cy="31" r="7"/><circle cx="63" cy="31" r="7"/>
      <path d="M24 62 V56 C24 46 30 42 40 42 C50 42 56 46 56 56 V62 Z"/>
      <path d="M24 55 H8 V51 C8 44 12 41 19 41 C22 41 25 42 27 44"/>
      <path d="M56 55 H72 V51 C72 44 68 41 61 41 C58 41 55 42 53 44"/>
    </g>
    <g id="i-person" class="icon">
      <circle cx="40" cy="8" r="5"/><circle cx="40" cy="72" r="5"/>
      <circle cx="8" cy="40" r="5"/><circle cx="72" cy="40" r="5"/>
      <path d="M45 9 C56 11 65 18 69 30"/><path d="M11 35 C14 22 24 13 35 10"/>
      <path d="M35 70 C22 67 13 58 10 45"/><path d="M69 50 C66 60 58 68 45 71"/>
      <circle cx="40" cy="32" r="6"/>
      <path d="M30 52 V47 C30 42 34 40 40 40 C46 40 50 42 50 47 V52 Z"/>
    </g>
    <g id="i-shield" class="icon">
      <path d="M40 4 L74 16 V40 C74 60 60 72 40 76 C20 72 6 60 6 40 V16 Z"/>
      <path d="M24 40 L36 52 L58 30"/>
    </g>
    <g id="i-scale" class="icon">
      <path d="M6 46 H28 V74 H6 Z"/>
      <path d="M22 58 L60 22"/><path d="M44 20 H62 V38"/>
      <path d="M26 6 H74 V54" stroke-dasharray="2 6"/>
      <path d="M26 6 V30 M50 54 H74" stroke-dasharray="2 6"/>
    </g>
    <g id="i-globe" class="icon">
      <circle cx="40" cy="40" r="34"/>
      <ellipse cx="40" cy="40" rx="15" ry="34"/>
      <path d="M7 30 H73 M10 54 H60"/>
      <path d="M4 50 C0 58 22 62 48 54 C60 50 70 44 74 38"/>
      <path d="M66 32 L75 37 L68 45"/>
    </g>
    <g id="i-up" fill="none" stroke="#fff" stroke-width="1.6" stroke-linecap="round" stroke-linejoin="round">
      <path d="M9 18 L15 12 L21 18"/>
    </g>
  </defs>
</svg>

<section class="panel panel-values">
  <div class="scrollbar"><div class="thumb" style="top:212px;height:48px"></div></div>
  <a class="to-top" style="top:391px" href="#" aria-label="Back to top"><svg viewBox="0 0 30 30"><use href="#i-up"/></svg></a>
</section>
<h2 class="section-title">SOMETHING ABOUT US</h2>
<p class="section-lead">These are the things that are part of everything we do.</p>

<div class="value" style="left:127px">
  <svg viewBox="0 0 80 80"><use href="#i-handshake"/></svg>
  <h3>Respect</h3>
  <ul>
    <li>We have a professional attitude combined with a respectful culture.</li>
    <li>Our outcomes create a positive environment for productivity and growth.</li>
  </ul>
</div>
<div class="value" style="left:395px">
  <svg viewBox="0 0 80 80"><use href="#i-team"/></svg>
  <h3>Commitment</h3>
  <ul>
    <li>Strong leadership committed to delivering our vision for Norvik9.</li>
    <li>To build and maintain strong and mutually beneficial relationships.</li>
  </ul>
</div>
<div class="value" style="left:664px">
  <svg viewBox="0 0 80 80"><use href="#i-person"/></svg>
  <h3>Responsible</h3>
  <ul>
    <li>Accepting ownership for decisions, actions, and behaviour.</li>
    <li>Driven by a desire to improve life globally by providing environmentally safe, ethical and equal working conditions and outcomes.</li>
  </ul>
</div>

<section class="panel panel-services">
  <div class="scrollbar"><div class="thumb" style="top:82px;height:64px"></div></div>
  <a class="to-top" style="top:391px" href="#" aria-label="Back to top"><svg viewBox="0 0 30 30"><use href="#i-up"/></svg></a>
</section>

<svg class="venn" viewBox="0 0 370 372" aria-label="Service areas diagram">
  <g stroke="#d9dede" stroke-width="3">
    <circle cx="183" cy="98" r="95" fill="var(--venn-top)"/>
    <circle cx="99" cy="185" r="95" fill="var(--venn-left)" fill-opacity="0.85"/>
    <circle cx="278" cy="185" r="95" fill="var(--venn-right)" fill-opacity="0.95"/>
    <circle cx="183" cy="272" r="95" fill="var(--venn-bottom)" fill-opacity="0.85"/>
  </g>
  <g fill="none" stroke="#fff" stroke-width="1.3">
    <circle cx="172" cy="34" r="11"/><circle cx="196" cy="34" r="11"/>
    <rect x="85" y="130" width="32" height="20" rx="2"/><path d="M101 150 V158 M92 158 H110"/>
    <rect x="262" y="146" width="34" height="24" rx="2" fill="#fff" fill-opacity="0.9"/>
    <path d="M170 306 l8 -4 8 4 -8 4z M186 306 l8 -4 8 4 -8 4z M178 296 l8 -4 8 4 -8 4z"/>
  </g>
  <text x="172" y="37" fill="#fff" font-size="7" font-family="Open Sans, sans-serif" text-anchor="middle">Dev</text>
  <text x="196" y="37" fill="#fff" font-size="7" font-family="Open Sans, sans-serif" text-anchor="middle">Ops</text>
</svg>
<div class="venn-label" style="left:241px;top:825px;width:140px;font-size:18px">DevOps<br>Infrastructure</div>
<div class="venn-label" style="left:137px;top:938px;width:90px;font-size:17px">Frontend<br>Software<br><span style="font-size:10px">(Platform<br>Admin Tool)</span></div>
<div class="venn-label" style="left:390px;top:962px;width:100px;font-size:18px">Backend<br>Software</div>
<div class="venn-label" style="left:251px;top:1082px;width:120px;font-size:18px">Blockchain</div>

<div class="feature" style="top:820px">
  <svg viewBox="0 0 80 80"><use href="#i-shield"/></svg>
  <h4>Security</h4>
  <p>Permissioned network - verified users, data protection and governance</p>
</div>
<div class="feature" style="top:920px">
  <svg viewBox="0 0 80 80"><use href="#i-scale"/></svg>
  <h4>Scalable</h4>
  <p>Modular architecture - optimised scalability and performance, flexible implementation</p>
</div>
<div class="feature" style="top:1020px">
  <svg viewBox="0 0 80 80"><use href="#i-globe"/></svg>
  <h4>Global</h4>
  <p>Enterprise friendly - adopted by leading enterprises including Quillmere, Brantova, Corvane, Deltrix, Elmwick and Fenroth</p>
</div>

</body>
</html>
```